Business card/Stationary for mobile ultrasound company
Corvin Ultrasound Services, LLC
Business card/Stationary for mobile ultrasound company -
Creative Brief
Use specific fonts
can use a combination of fonts similar to logo
Professional
Tessa Quillon RDMS, RVT, RCS
Owner
P.O. Box 482 Artesia, NM 88211-0482
4quillons@mailnest.example
I am currently getting a website designed so i will add a web address and an updated email address specifically for the business. I am torn as to use a one sided or 2 sided card. So im open. I would rather not have the address on the card. Thanks
Innovative mobile technology focused on improving the QUALITY of patient care. (The wording can change but along this idea)

```html
<!DOCTYPE html>
<html lang="en">
<head>
<meta charset="utf-8">
<title>Corvin Ultrasound Services — Stationery Set</title>
<link href="https://fonts.googleapis.com/css2?family=Cormorant+Garamond:wght@600&family=Lato:wght@400;700&display=swap" rel="stylesheet">
<style>
  :root{
    --stage:#4a4a4a;
    --stage-dark:#333333;
    --ink:#1a1a1a;
    --paper:#ffffff;
    --paper-shade:#eeeeee;
    --olive:#6b6b2a;
    --olive-light:#8d8d4a;
    --silver:#d8d8d8;
    --brand-grey:#8a8a8a;
    --grey-text:#777777;
    --flap-line:#cccccc;
    --flap-line-dark:#444444;
  }
  *{box-sizing:border-box;margin:0;padding:0}
  html,body{width:1200px;height:300px;overflow:hidden}
  body{
    background:linear-gradient(180deg,var(--stage),var(--stage-dark));
    position:relative;
    font-family:"Lato",sans-serif;
  }
  .brand-name{
    font-family:"Cormorant Garamond",serif;
    font-weight:600;
    color:var(--silver);
    line-height:1;
    white-space:nowrap;
  }
  .tagline{font-size:5px;letter-spacing:1px;color:var(--silver);white-space:nowrap}

  .hero-logo{position:absolute;left:40px;top:18px;width:220px;text-align:center}
  .hero-logo .brand-name{font-size:42px}
  .hero-logo .tagline{font-size:7px;letter-spacing:2px;margin-top:4px}

  .card{position:absolute;width:132px;height:74px;box-shadow:0 2px 4px rgba(0,0,0,.5);overflow:hidden}
  .card--dark{background:var(--ink)}
  .card--light{background:linear-gradient(160deg,var(--paper),var(--paper-shade))}
  .card .brand-name{position:absolute;left:12px;top:18px;font-size:24px}
  .card--light .brand-name{color:var(--brand-grey)}
  .card .tagline{position:absolute;left:12px;top:44px}
  .card--light .tagline{color:var(--grey-text)}
  .card .contact{position:absolute;right:8px;top:10px;font-size:5px;line-height:1.6;color:var(--silver);text-align:right;white-space:nowrap}
  .card .contact b{font-size:6px}
  .card svg{position:absolute;left:0;bottom:0}

  .sheet{position:absolute;top:20px;width:192px;height:263px;background:var(--paper);box-shadow:0 2px 5px rgba(0,0,0,.5);overflow:hidden}
  .sheet .brand-name{position:absolute;left:14px;top:12px;font-size:22px;color:var(--brand-grey)}
  .sheet .letter-contact{position:absolute;right:10px;top:14px;font-size:4.5px;line-height:1.6;color:var(--grey-text);text-align:right;white-space:nowrap}
  .sheet svg{position:absolute;left:0;bottom:0}

  .envelope{position:absolute;background:var(--paper);box-shadow:0 2px 5px rgba(0,0,0,.5);overflow:hidden}
  .envelope .brand-name{position:absolute;left:8px;top:7px;font-size:14px;color:var(--brand-grey)}
  .envelope .return{position:absolute;left:8px;top:24px;font-size:4px;line-height:1.5;color:var(--grey-text);white-space:nowrap}
  .envelope svg{position:absolute;left:0;bottom:0}
  .envelope--dark{background:var(--ink)}
  .envelope--olive{background:var(--olive)}
  .envelope .mark-dot{position:absolute;width:10px;height:10px;border-radius:50%;background:var(--silver);left:50%;margin-left:-5px}
</style>
</head>
<body>

<div class="hero-logo">
  <div class="brand-name">Corvin</div>
  <div class="tagline">ULTRASOUND SERVICES, LLC</div>
</div>

<div class="card card--dark" style="left:20px;top:108px">
  <div class="brand-name">Corvin</div>
  <div class="tagline">ULTRASOUND SERVICES, LLC</div>
</div>
<div class="card card--dark" style="left:158px;top:108px">
  <div class="contact"><b>Tessa Quillon</b><br>RDMS, RVT, RCS<br>Owner<br>4quillons@mailnest.example</div>
  <svg width="132" height="26" viewBox="0 0 132 26"><path d="M0 18 Q60 4 132 14 L132 26 L0 26Z" fill="var(--olive)"/><path d="M0 14 Q60 2 132 10" stroke="var(--silver)" stroke-width=".6" fill="none"/></svg>
</div>
<div class="card card--light" style="left:20px;top:196px">
  <div class="brand-name">Corvin</div>
  <div class="tagline">ULTRASOUND SERVICES, LLC</div>
</div>
<div class="card card--dark" style="left:158px;top:196px">
  <div class="brand-name">Corvin</div>
  <div class="tagline">ULTRASOUND SERVICES, LLC</div>
</div>

<div class="sheet" style="left:300px">
  <div class="brand-name">Corvin</div>
  <div class="letter-contact">P.O. Box 482 Calder Flats, NM 87999-0482<br>4quillons@mailnest.example</div>
  <svg width="192" height="40" viewBox="0 0 192 40"><path d="M0 26 Q90 6 192 22 L192 40 L0 40Z" fill="var(--olive)"/><path d="M0 20 Q90 2 192 16" stroke="var(--olive-light)" stroke-width="1" fill="none"/></svg>
</div>
<div class="sheet" style="left:510px">
  <svg width="192" height="40" viewBox="0 0 192 40"><path d="M0 26 Q90 6 192 22 L192 40 L0 40Z" fill="var(--olive)"/><path d="M0 20 Q90 2 192 16" stroke="var(--olive-light)" stroke-width="1" fill="none"/></svg>
</div>

<div class="envelope" style="left:716px;top:96px;width:200px;height:96px">
  <div class="brand-name">Corvin</div>
  <div class="return">P.O. Box 482 Calder Flats, NM 87999-0482</div>
  <svg width="200" height="26" viewBox="0 0 200 26"><path d="M0 16 Q100 2 200 12 L200 26 L0 26Z" fill="var(--olive)"/></svg>
</div>
<div class="envelope" style="left:716px;top:204px;width:200px;height:79px">
  <div class="brand-name">Corvin</div>
  <div class="return">P.O. Box 482 Calder Flats, NM 87999-0482</div>
  <svg width="200" height="22" viewBox="0 0 200 22"><path d="M0 14 Q100 2 200 10 L200 22 L0 22Z" fill="var(--olive)"/></svg>
</div>

<div class="envelope envelope--olive" style="left:956px;top:96px;width:220px;height:68px">
  <svg width="220" height="68" viewBox="0 0 220 68"><path d="M0 30 Q110 14 220 26 L220 68 L0 68Z" fill="var(--paper)"/></svg>
  <div class="mark-dot" style="top:10px"></div>
</div>
<div class="envelope envelope--dark" style="left:956px;top:168px;width:220px;height:66px">
  <svg width="220" height="66" viewBox="0 0 220 66"><path d="M0 0 L110 40 L220 0" stroke="var(--flap-line-dark)" stroke-width="1" fill="none"/></svg>
  <div class="mark-dot" style="top:16px"></div>
</div>
<div class="envelope" style="left:956px;top:226px;width:220px;height:60px">
  <svg width="220" height="60" viewBox="0 0 220 60"><path d="M0 0 L110 40 L220 0" stroke="var(--flap-line)" stroke-width="1" fill="none"/></svg>
</div>

</body>
</html>
```